Restaurant needs a vertical banner for fried catfish

Our restaurant is looking for an eye-catching 78.75in. x 36in. vertical physical banner ad for our fried catfish. Photos for the fried catfish will be provided as a reference but we will also accept anything similar to the photo. We will be using the following as our receptacle: https://www.plankoria.example/banner-stand/retractable-banner-stands/
The design must incorporate the following flavor texts:
Fried Catfish
Always Fresh!
Made from Scratch
Hand-cut Fillets
The Best Catfish in Texas
Served with fries, hush puppies, and a 32oz fountain drink
Also available by the pound!
The final design should be creative, professional, and eye-catching for customers.
Updates
Colors
Designer to choose colors to be used in the design.
Requirements
Must have
- We are open to any and all design elements, albeit the 'flavor texts' should not overpower, but complement the fried catfish photo. 'Fried Catfish' can be used in lieu of a main title/logo.
Nice to have
- Transparent or textured backgrounds that can encompass any or all part of the banner such as a cutting board, shadows, abstract, etc to show depth are a plus.
- Use of vectors or objects such as ribbons or shapes to encapsulate the 'flavor texts' are also encouraged.

```html
<!DOCTYPE html>
<html lang="en">
<head>
<meta charset="utf-8">
<title>Fried Catfish Banner</title>
<link rel="stylesheet" href="https://fonts.googleapis.com/css2?family=Anton&family=Oswald:wght@700&family=Roboto:wght@400;700&family=Lobster&display=swap">
<style>
  :root {
    --page: #f1f1f1;
    --banner: #e7e7e7;
    --copper: #b5682e;
    --copper-light: #c98445;
    --ink: #111111;
    --olive: #43401f;
    --badge: #6a2f1b;
    --white: #ffffff;
  }
  * { margin: 0; padding: 0; box-sizing: border-box; }
  html, body { width: 1200px; height: 1200px; overflow: hidden; background: var(--page); }
  .banner {
    position: absolute; left: 352px; top: 30px;
    width: 496px; height: 1140px;
    background: var(--banner);
    overflow: hidden;
    box-shadow: 0 6px 18px rgba(0,0,0,0.18);
  }
  .title {
    position: absolute; left: 0; right: 0; top: 52px;
    text-align: center;
    font-family: "Oswald", sans-serif; font-weight: 700;
    font-size: 74px; line-height: 1; letter-spacing: 0;
    color: var(--copper);
    transform: scaleY(1.08);
  }
  .swoosh { position: absolute; left: 0; top: 145px; width: 496px; height: 50px; }
  .food-photo {
    position: absolute; left: 0; top: 175px; width: 496px; height: 305px;
    background:
      radial-gradient(ellipse at 55% 55%, #b77a35 0%, #8f5a24 35%, transparent 60%),
      radial-gradient(ellipse at 30% 78%, #e8c36c 0%, transparent 35%),
      radial-gradient(ellipse at 12% 20%, #c8432a 0%, transparent 18%),
      linear-gradient(180deg, #9b7b55 0%, #d9d2c4 55%, #8a6f4f 100%);
    clip-path: path("M0 14 Q248 -4 496 0 L496 292 Q248 308 0 305 Z");
  }
  .badge {
    position: absolute; left: 352px; top: 408px; width: 138px; height: 138px;
    border-radius: 50%; background: var(--badge);
    border: 3px solid var(--white);
    display: flex; flex-direction: column; align-items: center; justify-content: center;
    font-family: "Lobster", cursive; color: var(--white);
    font-size: 36px; line-height: 0.95; transform: rotate(-6deg);
  }
  .pitch { position: absolute; left: 30px; top: 500px; color: var(--ink); }
  .pitch .made {
    display: block; font-family: "Anton", sans-serif; font-size: 52px; line-height: 1.08;
  }
  .pitch .scratch {
    display: block; font-family: "Anton", sans-serif; font-size: 86px; line-height: 0.98;
    margin-top: -4px;
  }
  .pitch .fillets {
    display: block; font-family: "Roboto", sans-serif; font-size: 45px; line-height: 1.1;
  }
  .ribbon {
    position: absolute; left: 10px; top: 722px; width: 476px; height: 58px;
    background: var(--olive);
    color: var(--white);
    font-family: "Roboto", sans-serif; font-size: 34px;
    display: flex; align-items: center; justify-content: center;
    box-shadow: 0 10px 8px -6px rgba(0,0,0,0.55);
  }
  .ribbon .star { font-size: 20px; margin: 0 8px; }
  .served { position: absolute; left: 43px; top: 810px; }
  .served h2 {
    font-family: "Oswald", sans-serif; font-weight: 700; font-size: 23px; line-height: 1.1;
    color: var(--copper);
  }
  .served p {
    font-family: "Roboto", sans-serif; font-size: 18px; color: var(--ink); margin-top: 6px;
  }
  .by-pound {
    position: absolute; left: 0; right: 0; top: 926px; text-align: center;
    font-family: "Roboto", sans-serif; font-size: 23px; color: var(--ink);
  }
  .by-pound .underline {
    border-bottom: 3px dotted var(--copper); padding-bottom: 5px;
  }
  .base-band {
    position: absolute; left: 0; bottom: 0; width: 496px; height: 59px;
    background: var(--copper);
  }
</style>
</head>
<body>
  <main class="banner">
    <h1 class="title">FRIED CATFISH</h1>
    <svg class="swoosh" viewBox="0 0 496 50" aria-hidden="true">
      <path d="M0 22 Q260 18 496 0 L496 14 Q300 28 40 28 Z" fill="var(--copper)"/>
    </svg>
    <div class="food-photo" role="img" aria-label="Plate of fried catfish fillets with fries, hush puppies, tartar sauce and fresh tomatoes"></div>
    <div class="badge"><span>Always</span><span>Fresh!</span></div>
    <section class="pitch">
      <span class="made">Made from</span>
      <span class="scratch">Scratch</span>
      <span class="fillets">Hand-Cut Fillets</span>
    </section>
    <div class="ribbon"><span class="star">★</span>The Best Catfish in Texas<span class="star">★</span></div>
    <section class="served">
      <h2>Served with:</h2>
      <p>Fries | Hush Puppies | and a 32oz Fountain Drink</p>
    </section>
    <p class="by-pound">Also <strong>available</strong> <span class="underline">by the pound!</span></p>
    <div class="base-band"></div>
  </main>
</body>
</html>
```